Lifestyle blog needs a website

I have a blog called Bright Years Ahead. Logo has been done and I also have the wordpress site with a theme already added to it.

The basics are there but I need design expertise to put everything together, make it look great and ready for me to go and in and start using. Basically what is there at the moment needs to be deleted and start again (not a lot - just me playing around). I am not attached to the theme and am happy to go with whatever ideas you can come up with. At the moment I am looking at 3 lifestyle categories (Fashion, Fitness, Feelings) with a contact page so not an extensive build.

Audience will be women over 40 but please don't make this 'frumpy' - it is aimed at the women who act, look and feel younger than their age and so 'pink & fluffy' and 'old & solid' is not the look I am going for.

My deepest apologies for the delay in responding to designs. I had a family matter which took meant I was unable to spend the quality time required to review. I will therefore be reviewing and deciding over this weekend. Once again, my sincere apologies.

Women over 40

• Feeling of being targeted at old market

```html
<!DOCTYPE html>
<html lang="en">
<head>
<meta charset="utf-8">
<title>Bright Years Ahead</title>
<link href="https://fonts.googleapis.com/css2?family=Bodoni+Moda:wght@400;500&family=Jost:wght@400;500&display=swap" rel="stylesheet">
<style>
:root{
  --red:#e8343c;
  --blue:#3fb6e6;
  --ink:#3e4450;
  --text:#5a5a5a;
  --muted:#8a8a8a;
  --page-grey:#efefef;
  --card-grey:#f4f4f4;
  --line:#c9c9c9;
  --white:#ffffff;
}
*{box-sizing:border-box;margin:0;padding:0}
html,body{width:1200px;height:2871px;overflow:hidden}
body{position:relative;background:var(--white);font-family:"Jost",sans-serif;color:var(--text)}
.abs{position:absolute}
.serif{font-family:"Bodoni Moda",serif;color:#222}
.photo{position:absolute}
.btn{position:absolute;display:flex;align-items:center;justify-content:center;border:2px solid var(--red);color:var(--red);font-size:12px;letter-spacing:1px;background:var(--white);font-weight:500}
.btn.solid{background:var(--red);color:var(--white)}
.tag{position:absolute;background:var(--blue);color:var(--white);font-size:11px;letter-spacing:1.5px;display:flex;align-items:center;justify-content:center;font-weight:500}
.circle{position:absolute;border:2px solid var(--red);border-radius:50%}
.circle.solid{background:var(--red)}
.circle::after{content:"";position:absolute;left:50%;top:50%;width:6px;height:6px;margin:-3px 0 0 -3px;border-radius:50%;background:var(--red)}
.circle.solid::after{background:var(--white)}

/* top grey area */
.top-band{left:0;top:0;width:1200px;height:1125px;background:var(--page-grey)}
.logo{left:77px;top:30px;font-family:"Bodoni Moda",serif;font-size:26px;line-height:26px;color:var(--red);font-weight:500;width:160px}
.nav{top:40px;font-size:14px;color:#444;letter-spacing:.5px}
.nav.active{color:var(--red);font-weight:500}
.social-label{left:852px;top:40px;font-size:14px;color:var(--red);font-weight:500}

/* hero */
.hero{left:77px;top:96px;width:1018px;height:482px;background:var(--white)}
.hero-title{left:153px;top:208px;font-size:29px;line-height:38px;width:480px;white-space:nowrap}
.hero-rule{left:128px;top:306px;width:54px;height:1px;background:var(--line)}
.hero-text{left:207px;top:298px;font-size:13px;line-height:20px;width:220px}
.dot{position:absolute;width:6px;height:6px;border-radius:50%;background:#555}
.dot.on{width:8px;height:8px;background:var(--red)}
.arrow{position:absolute;width:30px;height:30px;border-radius:50%;border:1.5px solid #555;display:flex;align-items:center;justify-content:center}
.arrow.next{border-color:var(--red)}

/* section headings */
.section-title{font-size:30px;text-align:center}
.rule{position:absolute;height:1px;background:var(--line)}

/* category cards */
.cat-card{position:absolute;top:699px;width:281px;height:363px}
.cat-panel{position:absolute;left:15px;top:178px;width:251px;height:168px;background:rgba(255,255,255,.95)}
.cat-panel .tag{left:72px;top:-9px;width:106px;height:20px}
.cat-title{position:absolute;left:0;top:34px;width:100%;text-align:center;font-size:16px;line-height:18px}
.cat-panel .btn{left:61px;top:111px;width:128px;height:32px}

/* blog */
.post-box{left:230px;top:1447px;width:358px;height:232px;background:var(--card-grey);border-top:4px solid var(--blue);text-align:center}
.date{color:var(--red);font-size:13px;letter-spacing:.5px}
.post-title{font-size:17px;line-height:21px}
.red-rule{width:40px;height:2px;background:var(--red);margin:0 auto}
.excerpt{font-size:12.5px;line-height:19px;color:var(--muted)}
.mini{position:absolute;top:1730px;width:205px;height:431px}
.mini .photo{left:0;top:0;width:205px;height:203px}
.mini .tag{left:0;top:0;width:88px;height:20px}
.mini-body{position:absolute;left:0;top:203px;width:205px;height:228px;background:var(--card-grey);text-align:center;padding-top:26px}
.mini-body .post-title{font-size:15px;line-height:20px;margin-top:10px}
.mini-body .red-rule{margin-top:10px}
.mini-body .excerpt{margin:10px auto 0;width:170px;font-size:11.5px;line-height:17px}
.mini .btn{left:45px;top:411px;width:115px;height:33px}

/* sidebar */
.widget{position:absolute;left:817px;width:307px;border:1.5px solid #9a9ea6;border-top:none}
.widget-head{position:absolute;left:842px;width:257px;height:46px;background:var(--ink);color:var(--white);font-family:"Bodoni Moda",serif;font-size:18px;display:flex;align-items:center;padding-left:24px}
.widget-text{font-size:12.5px;line-height:19px;color:var(--muted)}
.pill{position:absolute;height:21px;border:1px solid #9a9ea6;font-size:10px;letter-spacing:1px;display:flex;align-items:center;justify-content:center;color:#555}
.pill.on{background:var(--blue);border-color:var(--blue);color:var(--white)}

/* photo strip */
.strip-tile{position:absolute;top:2368px;width:200px;height:201px}

/* footer */
.footer-bar{left:0;top:2821px;width:1200px;height:50px;background:var(--ink)}
</style>
</head>
<body>

<div class="abs top-band"></div>

<!-- header -->
<div class="abs logo">Bright Years Ahead</div>
<div class="abs nav active" style="left:330px">-- Home --</div>
<div class="abs nav" style="left:444px">About Us</div>
<div class="abs nav" style="left:549px">Categories</div>
<div class="abs nav" style="left:664px">Contact Us</div>
<svg class="abs" style="left:791px;top:41px" width="14" height="14" viewBox="0 0 14 14"><circle cx="6" cy="6" r="4.5" fill="none" stroke="#444" stroke-width="2"/><line x1="9.5" y1="9.5" x2="13" y2="13" stroke="#444" stroke-width="2"/></svg>
<div class="abs social-label">Get Social:</div>
<div class="circle" style="left:935px;top:32px;width:32px;height:32px"></div>
<div class="circle" style="left:974px;top:32px;width:32px;height:32px"></div>
<div class="circle" style="left:1013px;top:32px;width:32px;height:32px"></div>
<div class="circle" style="left:1052px;top:32px;width:32px;height:32px"></div>
<div class="circle" style="left:1091px;top:32px;width:32px;height:32px"></div>

<!-- hero -->
<div class="abs hero"></div>
<div class="photo" role="img" aria-label="Woman in sunglasses at the beach looking at her phone" style="left:436px;top:96px;width:688px;height:402px;background:linear-gradient(120deg,#7fa9bd 0%,#b9d0da 40%,#d8c4a8 70%,#c9b79a 100%)"></div>
<div class="abs serif hero-title">Excepteur occaecat there<br>contrary to popular belief, lorem</div>
<div class="hero-rule abs"></div>
<div class="abs hero-text">There are many variations of an passages of Lorem Ipsum...</div>
<div class="btn" style="left:207px;top:369px;width:128px;height:31px">Explore More</div>
<div class="dot" style="left:461px;top:537px"></div>
<div class="dot" style="left:472px;top:537px"></div>
<div class="dot on" style="left:482px;top:536px"></div>
<div class="dot" style="left:494px;top:537px"></div>
<div class="dot" style="left:504px;top:537px"></div>
<div class="arrow" style="left:999px;top:525px"><svg width="14" height="10" viewBox="0 0 14 10"><path d="M13 5H2M5 1 1 5l4 4" fill="none" stroke="#555" stroke-width="1.5"/></svg></div>
<div class="arrow next" style="left:1038px;top:525px"><svg width="14" height="10" viewBox="0 0 14 10"><path d="M1 5h11M9 1l4 4-4 4" fill="none" stroke="#e8343c" stroke-width="1.5"/></svg></div>

<!-- categories -->
<div class="rule" style="left:455px;top:657px;width:54px"></div>
<div class="abs serif section-title" style="left:500px;top:636px;width:200px">Categories</div>
<div class="rule" style="left:693px;top:657px;width:54px"></div>

<div class="cat-card" style="left:153px">
  <div class="photo" role="img" aria-label="Blonde woman in sunglasses in a golden field" style="left:0;top:0;width:281px;height:363px;background:linear-gradient(160deg,#c9a27a,#e4cfb2 45%,#b8895a)"></div>
  <div class="cat-panel"><div class="tag">FASHION</div><div class="cat-title serif">Contrary to<br>popular belief, Lorem<br>Ipsum site...</div><div class="btn">Learn More</div></div>
</div>
<div class="cat-card" style="left:459px">
  <div class="photo" role="img" aria-label="Woman stretching outdoors under a blue sky" style="left:0;top:0;width:282px;height:363px;background:linear-gradient(180deg,#5c9fd1,#a8cbe6 45%,#d9cba4 75%,#b58e52)"></div>
  <div class="cat-panel"><div class="tag">FITNESS</div><div class="cat-title serif">Contrary to<br>popular belief, Lorem<br>Ipsum site...</div><div class="btn solid">Learm More</div></div>
</div>
<div class="cat-card" style="left:766px">
  <div class="photo" role="img" aria-label="Couple standing together in a snowy forest" style="left:0;top:0;width:281px;height:363px;background:linear-gradient(160deg,#e6e8ec,#cfd3da 50%,#8a7d78)"></div>
  <div class="cat-panel"><div class="tag">FEELINGS</div><div class="cat-title serif">Contrary to<br>popular belief, Lorem<br>Ipsum site...</div><div class="btn">Learn More</div></div>
</div>

<!-- latest blog -->
<div class="rule" style="left:260px;top:1205px;width:52px"></div>
<div class="abs serif section-title" style="left:308px;top:1184px;width:200px">Latest Blog</div>
<div class="rule" style="left:503px;top:1205px;width:52px"></div>

<div class="photo" role="img" aria-label="Woman in sunglasses working at a desk with a computer" style="left:77px;top:1246px;width:664px;height:280px;background:linear-gradient(110deg,#b7bcc2,#6e7278 40%,#3b3d42 70%,#7a7f86)"></div>
<div class="tag" style="left:77px;top:1246px;width:107px;height:21px">FASHION</div>
<div class="abs post-box">
  <div class="date" style="margin-top:38px">&#9719; SEP 18<sup style="font-size:8px">TH</sup>, 2017</div>
  <div class="serif post-title" style="margin-top:10px">Contrary to popular belief,<br>Lorem Ipsum is not simply random.</div>
  <div class="red-rule" style="margin-top:14px"></div>
  <div class="excerpt" style="margin:22px auto 0;width:290px">There are many variations of passages of Lorem Ipsum available, but the majority have suffered alteration in some form, by...</div>
</div>
<div class="btn solid" style="left:352px;top:1663px;width:113px;height:33px">Read More</div>

<div class="mini" style="left:77px">
  <div class="photo" role="img" aria-label="Woman doing a yoga split on a terrace" style="background:linear-gradient(170deg,#d7b98a,#c39c6c 50%,#5a6a82)"></div>
  <div class="tag">FITNESS</div>
  <div class="mini-body"><div class="date">&#9719; AUG 11<sup style="font-size:7px">TH</sup>, 2017</div><div class="serif post-title">Contrary to popular<br>belief, lorem ipsum sit.</div><div class="red-rule"></div><div class="excerpt">There are many variations of passages of Lorem Ipsum available, but the majority have done work...</div></div>
  <div class="btn">Read More</div>
</div>
<div class="mini" style="left:306px">
  <div class="photo" role="img" aria-label="Smiling couple embracing" style="background:linear-gradient(160deg,#9fa7b0,#c8a68a 50%,#4c5a73)"></div>
  <div class="tag">FEELINGS</div>
  <div class="mini-body"><div class="date">&#9719; AUG 11<sup style="font-size:7px">TH</sup>, 2017</div><div class="serif post-title">Contrary to popular<br>belief, lorem ipsum sit.</div><div class="red-rule"></div><div class="excerpt">There are many variations of passages of Lorem Ipsum available, but the majority have done work...</div></div>
  <div class="btn">Read More</div>
</div>
<div class="mini" style="left:536px">
  <div class="photo" role="img" aria-label="Woman sitting on a kitchen counter" style="background:linear-gradient(160deg,#e2e2e2,#a9a9a9 50%,#3a3a3a)"></div>
  <div class="tag">LIFESTYLE</div>
  <div class="mini-body"><div class="date">&#9719; AUG 11<sup style="font-size:7px">TH</sup>, 2017</div><div class="serif post-title">Contrary to popular<br>belief, lorem ipsum sit.</div><div class="red-rule"></div><div class="excerpt">There are many variations of passages of Lorem Ipsum available, but the majority have done work...</div></div>
  <div class="btn">Read More</div>
</div>

<div class="dot" style="left:78px;top:2219px"></div>
<div class="dot" style="left:88px;top:2219px"></div>
<div class="dot on" style="left:97px;top:2218px"></div>
<div class="dot" style="left:108px;top:2219px"></div>
<div class="dot" style="left:118px;top:2219px"></div>
<svg class="abs" style="left:693px;top:2214px" width="46" height="16" viewBox="0 0 46 16"><path d="M14 8H2M6 4 2 8l4 4" fill="none" stroke="#555" stroke-width="1.5"/><line x1="23" y1="2" x2="23" y2="14" stroke="#999"/><path d="M32 8h12M40 4l4 4-4 4" fill="none" stroke="#e8343c" stroke-width="1.5"/></svg>

<!-- sidebar -->
<div class="widget" style="top:1213px;height:387px"></div>
<div class="widget-head" style="top:1190px">About Me</div>
<div class="photo" role="img" aria-label="Woman in a pink hat sitting in a sunny meadow" style="left:842px;top:1263px;width:257px;height:161px;background:linear-gradient(160deg,#e9ddb0,#a9c27a 55%,#6f9a4e)"></div>
<div class="abs widget-text" style="left:842px;top:1443px;width:250px">There are many variations of passages of Lorem Ipsum available, but the majority have the suffered alteration in ev...</div>
<div class="btn" style="left:842px;top:1539px;width:128px;height:32px">Discover More</div>

<div class="widget" style="top:1650px;height:111px"></div>
<div class="widget-head" style="top:1627px">Follow Me</div>
<div class="circle" style="left:842px;top:1699px;width:38px;height:38px"></div>
<div class="circle solid" style="left:896px;top:1699px;width:38px;height:38px"></div>
<div class="circle" style="left:950px;top:1699px;width:38px;height:38px"></div>
<div class="circle" style="left:1004px;top:1699px;width:38px;height:38px"></div>
<div class="circle" style="left:1058px;top:1699px;width:38px;height:38px"></div>

<div class="widget" style="top:1811px;height:199px"></div>
<div class="widget-head" style="top:1788px">Subscribe</div>
<div class="abs widget-text" style="left:842px;top:1858px;width:260px;color:#666">Subscribe to my newsletter to get latest scoop right to your inbox.</div>
<div class="abs" style="left:842px;top:1912px;width:257px;height:33px;border:1px solid #ccc;font-size:11px;color:#999;padding:9px 10px">Enter Your Email...</div>
<div class="btn solid" style="left:842px;top:1954px;width:96px;height:33px">Send</div>

<div class="widget" style="top:2060px;height:166px"></div>
<div class="widget-head" style="top:2038px">Tag</div>
<div class="pill" style="left:842px;top:2111px;width:126px">HEALTH &amp; BEAUTY</div>
<div class="pill" style="left:974px;top:2111px;width:125px">MEDICINE &amp; MORE</div>
<div class="pill" style="left:842px;top:2143px;width:55px">FOOD</div>
<div class="pill on" style="left:905px;top:2143px;width:75px">FASHION</div>
<div class="pill" style="left:988px;top:2143px;width:80px">FITNESS</div>
<div class="pill" style="left:842px;top:2176px;width:80px">FEELINGS</div>
<div class="pill" style="left:929px;top:2176px;width:76px">LIFESTYLE</div>

<!-- photo strip -->
<div class="rule" style="left:474px;top:2302px;width:50px"></div>
<div class="abs serif section-title" style="left:500px;top:2280px;width:200px">Snapshots</div>
<div class="rule" style="left:676px;top:2302px;width:50px"></div>
<div class="abs" style="left:450px;top:2322px;width:300px;text-align:center;font-size:11px;color:var(--red)">follow@brightyearsahead</div>

<div class="strip-tile" role="img" aria-label="Person sitting on autumn leaves" style="left:0;background:linear-gradient(160deg,#8c6a4a,#b89072 50%,#4e5a6e)"></div>
<div class="strip-tile" role="img" aria-label="Woman walking through a field" style="left:200px;background:linear-gradient(180deg,#5b5e5a,#7b7460 50%,#3d3a30)"></div>
<div class="strip-tile" role="img" aria-label="Woman in a hat by a lake" style="left:400px;background:linear-gradient(180deg,#c9d4da,#93a6ad 50%,#4b5650)"></div>
<div class="strip-tile" role="img" aria-label="Person with arms open on an autumn path" style="left:600px;background:linear-gradient(160deg,#b07a44,#6a5a3e 50%,#2f3a2e)"></div>
<div class="strip-tile" role="img" aria-label="Sneakers on a stone ledge" style="left:800px;background:linear-gradient(180deg,#2f3f4a,#6e7478 50%,#a8a8a6)"></div>
<div class="strip-tile" role="img" aria-label="Person holding a camera" style="left:1000px;background:linear-gradient(160deg,#e6e2dc,#a79f96 50%,#3e3a38)"></div>

<!-- footer -->
<div class="abs" style="left:450px;top:2650px;width:300px;text-align:center;font-family:'Bodoni Moda',serif;font-size:34px;line-height:36px;color:var(--red);font-weight:500">Bright Years Ahead</div>
<div class="abs" style="left:300px;top:2742px;width:600px;text-align:center;font-size:13px;line-height:20px;color:#666">There are many variations of passages of Lorem Ipsum available, but the majority have suffered alteration in some form, by injected humour, or randomised.</div>
<div class="abs footer-bar"></div>
<div class="abs" style="left:153px;top:2838px;font-size:12px;color:#d8dbe0">© 2016 Bright Years Ahead. All Rights Reserved</div>
<div class="abs" style="left:995px;top:2821px;width:54px;height:50px;background:var(--red);display:flex;align-items:center;justify-content:center"><svg width="12" height="16" viewBox="0 0 12 16"><path d="M6 15V2M1 7l5-5 5 5" fill="none" stroke="#fff" stroke-width="1.8"/></svg></div>

</body>
</html>
```